Hot Offer banner for product listing page

Hi, we need a banner in the dimensions 210x390px which will be shown in the product listing on our online shop. There are 18 products and in between randomly there should be 3 banners with three different information.
first banner: fast delivery
The idea is to show a stove which is very "fast". Maybe you can make an effect like in Driftcraft Valorne when they activate the warp drive or something similar. Anyway, the banner should indicate that the delivery is very fast for this product.

second banner: Advantage banner
We would like to have a banner which names all our advantages in our online shop. this is the list of advantages:
- over 200,000 satisfied customers
- Best price guarantee
- thousands of devices in stock
- Top ratings

I attached you some examples, just to give you an idea.

```html
<!DOCTYPE html>
<html lang="en">
<head>
<meta charset="utf-8">
<title>Shop Banners – Fast Delivery &amp; Advantages</title>
<link rel="stylesheet" href="https://fonts.googleapis.com/css2?family=PT+Serif&family=Saira:wght@400&display=swap">
<style>
  :root {
    --page-bg: #ffffff;
    --orange-top: #ef9533;
    --orange-mid: #e4713a;
    --orange-bottom: #d74b33;
    --stove-shade: rgba(190, 80, 30, 0.35);
    --panel-light: #f7f8fa;
    --headline-grey: #4b4e53;
    --line-white: #ffffff;
    --illustration-tint: rgba(255, 255, 255, 0.22);
  }
  * { margin: 0; padding: 0; box-sizing: border-box; }
  html, body { width: 1200px; height: 1078px; overflow: hidden; background: var(--page-bg); }
  .canvas { position: relative; width: 1200px; height: 1078px; }

  .banner { position: absolute; top: 52px; width: 514px; height: 956px; overflow: hidden; }
  .banner--delivery { left: 48px; background: var(--panel-light); }
  .banner--advantages { left: 627px; }

  .stove-backdrop {
    position: absolute; inset: 0;
    background:
      radial-gradient(ellipse 32% 48% at 50% 58%, var(--stove-shade) 0%, rgba(190, 80, 30, 0) 100%),
      linear-gradient(180deg, var(--orange-top) 0%, var(--orange-mid) 55%, var(--orange-bottom) 100%);
  }
  .delivery-hero { position: absolute; left: 0; top: 0; width: 514px; height: 660px; }

  .rocket-illustration {
    position: absolute; left: 124px; top: 181px; width: 267px; height: 269px;
    border-radius: 18px;
    background: radial-gradient(ellipse at 50% 50%, var(--illustration-tint) 0%, rgba(255, 255, 255, 0.08) 100%);
  }

  .delivery-title {
    position: absolute; left: 0; right: 0; top: 713px;
    font-family: "PT Serif", Georgia, serif; font-weight: 400;
    font-size: 74px; line-height: 87px; color: var(--headline-grey);
    text-align: center; letter-spacing: -1px;
  }

  .advantage-list { position: absolute; inset: 0; list-style: none; }
  .advantage { position: absolute; left: 0; right: 0; text-align: center; }
  .advantage-badge { display: block; margin: 0 auto; width: 104px; height: 104px; }
  .advantage-label {
    display: block; margin-top: 16px;
    font-family: "Saira", "Exo 2", sans-serif; font-size: 27px; line-height: 35px;
    color: var(--line-white); letter-spacing: 0.3px;
  }
  .advantage--customers { top: 49px; }
  .advantage--price { top: 285px; }
  .advantage--stock { top: 488px; }
  .advantage--ratings { top: 727px; }
</style>
</head>
<body>
<div class="canvas">

  <section class="banner banner--delivery">
    <svg class="delivery-hero" viewBox="0 0 514 660" role="img" aria-label="Photo of a round wood-burning stove with burning fire beside stacked firewood, tinted orange">
      <defs>
        <linearGradient id="heroTint" x1="0" y1="0" x2="0" y2="1">
          <stop offset="0" stop-color="#ef9533"/>
          <stop offset="0.55" stop-color="#e4713a"/>
          <stop offset="1" stop-color="#d4432f"/>
        </linearGradient>
        <radialGradient id="heroStove" cx="0.5" cy="0.6" r="0.45">
          <stop offset="0" stop-color="#be501e" stop-opacity="0.35"/>
          <stop offset="1" stop-color="#be501e" stop-opacity="0"/>
        </radialGradient>
      </defs>
      <path d="M0 0 H514 V523 Q257 749 0 526 Z" fill="url(#heroTint)"/>
      <path d="M0 0 H514 V523 Q257 749 0 526 Z" fill="url(#heroStove)"/>
    </svg>
    <div class="rocket-illustration" role="img" aria-label="Line illustration of a rocket launching with speed lines, stars and planets"></div>
    <h2 class="delivery-title">Fast<br>Delivery</h2>
  </section>

  <section class="banner banner--advantages">
    <div class="stove-backdrop" role="img" aria-label="Photo of a round wood-burning stove in a living room, tinted orange"></div>
    <svg width="0" height="0" style="position:absolute">
      <defs>
        <radialGradient id="badgeFill" cx="0.5" cy="0.45" r="0.55">
          <stop offset="0" stop-color="#f8a865"/>
          <stop offset="1" stop-color="#ee7e2b"/>
        </radialGradient>
      </defs>
    </svg>
    <ul class="advantage-list">
      <li class="advantage advantage--customers">
        <svg class="advantage-badge" viewBox="0 0 104 104" fill="none" stroke="#fff" stroke-width="2.6" stroke-linejoin="round">
          <circle cx="52" cy="52" r="49" fill="url(#badgeFill)" stroke-width="3.6"/>
          <path d="M33 52 V47 Q33 28 52 28 Q71 28 71 47 V52"/>
          <rect x="27" y="52" width="8" height="15"/>
          <rect x="69" y="52" width="8" height="15"/>
          <path d="M73 67 Q73 73 60 73 H55"/>
          <circle cx="52" cy="73" r="2.5"/>
        </svg>
        <span class="advantage-label">Over 200,000 Satisfied<br>Customers</span>
      </li>
      <li class="advantage advantage--price">
        <svg class="advantage-badge" viewBox="0 0 104 104" fill="none" stroke="#fff" stroke-width="2.4" stroke-linejoin="round">
          <circle cx="52" cy="52" r="49" fill="url(#badgeFill)" stroke-width="3.6"/>
          <path d="M52 20 L58 24 L65 23 L68 29 L74 33 L72 40 L75 46 L70 51 L70 58 L63 60 L58 65 L52 62 L46 65 L41 60 L34 58 L34 51 L29 46 L32 40 L30 33 L36 29 L39 23 L46 24 Z"/>
          <circle cx="52" cy="43" r="13"/>
          <path d="M46 43 L50 47 L58 39" stroke-linecap="round"/>
          <path d="M42 63 V80 L52 74 L62 80 V63"/>
        </svg>
        <span class="advantage-label">Best Price Guarantee</span>
      </li>
      <li class="advantage advantage--stock">
        <svg class="advantage-badge" viewBox="0 0 104 104" fill="none" stroke="#fff" stroke-width="2.4" stroke-linejoin="round">
          <circle cx="52" cy="52" r="49" fill="url(#badgeFill)" stroke-width="3.6"/>
          <rect x="46" y="28" width="17" height="17"/>
          <rect x="33" y="45" width="19" height="19"/>
          <rect x="52" y="45" width="19" height="19"/>
          <path d="M51 28 V33 H58 V28 M39 45 V50 H46 V45 M58 45 V50 H65 V45"/>
          <rect x="25" y="64" width="54" height="8"/>
        </svg>
        <span class="advantage-label">Thousands Of Devices<br>In Stock</span>
      </li>
      <li class="advantage advantage--ratings">
        <svg class="advantage-badge" viewBox="0 0 104 104" fill="none" stroke="#fff" stroke-width="2.4" stroke-linejoin="round">
          <circle cx="52" cy="52" r="49" fill="url(#badgeFill)" stroke-width="3.6"/>
          <polygon transform="translate(30 55)" points="0,-11 3,-4 10,-3 5,2 6,9 0,5 -6,9 -5,2 -10,-3 -3,-4"/>
          <polygon transform="translate(52 45)" points="0,-11 3,-4 10,-3 5,2 6,9 0,5 -6,9 -5,2 -10,-3 -3,-4"/>
          <polygon transform="translate(74 55)" points="0,-11 3,-4 10,-3 5,2 6,9 0,5 -6,9 -5,2 -10,-3 -3,-4"/>
        </svg>
        <span class="advantage-label">Top Ratings</span>
      </li>
    </ul>
  </section>

</div>
</body>
</html>
```